New Look Driving School Project

Current website:
www. kelmorawheelacademy.com

Websites that we like (use content and courses from here as well):
https://www. tollbenroadclass.com

We are looking for a fresh looking driving school website that is easy for students to find the course they are looking for, the price, and allow them to book a lesson all on our website. We would like for this website to have multiple pages: Home, Teen Courses, Adult Courses, About Us, Contact, FAQ, Blog, Requirements.

Target Market(s)

Students in High School or Parents

Industry/Entity Type

Education

Coding

Coded - Design and coding required

Number of Pages Required

5+ page

Font styles to use
Serif
Sans Serif

Colors

Designer to choose colors to be used in the design.

Requirements
Must have
• Must have a form submission and payment processing option. Must have the ability to pick a course, see available times, and process their payment online. MUST BE MOBILE FRIENDLY DESIGN.
Nice to have
• Nice to have a clean format, with big bold fonts.
Should not have
• Should not have a lot of sliders or animations. Should be very fast loading on mobile. Keep it simple but easy to read and elegant.

```html
<!DOCTYPE html>
<html lang="en">
<head>
<meta charset="utf-8">
<title>Kelmora Wheel Academy</title>
<link href="https://fonts.googleapis.com/css2?family=Ubuntu:wght@400;500;700&family=Open+Sans:wght@400;600;700&display=swap" rel="stylesheet">
<style>
:root{
  --red:#c21f2d;
  --yellow:#fff200;
  --ink:#222;
  --muted:#555;
  --light:#f2f2f2;
  --dark:#1a1a1a;
  --white:#fff;
}
*{box-sizing:border-box;margin:0;padding:0}
html,body{width:1200px;height:4523px;overflow:hidden}
body{font-family:"Open Sans",sans-serif;color:var(--ink);background:var(--white);position:relative}
h1,h2,h3,h4{font-family:"Ubuntu",sans-serif}
.btn{display:inline-flex;align-items:center;justify-content:center;background:var(--yellow);color:#111;font-family:"Ubuntu",sans-serif;font-weight:700;font-size:14px;text-transform:uppercase;text-decoration:none;letter-spacing:.5px}
.section-title{color:var(--red);font-size:32px;font-weight:500;text-align:center}

/* header */
.site-header{position:absolute;top:0;left:0;width:1200px;height:60px;display:flex;align-items:center;justify-content:space-between;padding:0 81px;background:var(--white)}
.brand{color:var(--red);font-family:"Ubuntu",sans-serif;font-weight:700;font-size:24px}
.nav{display:flex;gap:30px;font-family:"Ubuntu",sans-serif;font-size:14px}
.nav a{color:var(--ink);text-decoration:none}
.nav a.active{color:var(--red)}

/* hero */
.hero{position:absolute;top:60px;left:0;width:1200px;height:658px;background:linear-gradient(100deg,#3c3c3e 0%,#7a7576 35%,#d9c6c0 60%,#efe3dc 100%)}
.hero-copy{position:absolute;left:81px;top:385px;width:460px;color:var(--white)}
.hero-copy h1{font-size:31px;font-weight:700;text-transform:uppercase;letter-spacing:.5px}
.hero-copy p{font-size:14px;line-height:24px;margin-top:16px}
.hero-copy .btn{margin-top:22px;width:185px;height:45px;text-transform:none;font-size:15px}

/* about + form */
.about{position:absolute;top:718px;left:0;width:1200px;height:442px;background:var(--light)}
.about-copy{position:absolute;left:81px;top:92px;width:520px}
.about-copy h2{color:var(--red);font-size:34px;font-weight:500}
.about-copy .lead{color:var(--red);font-weight:700;font-size:16px;line-height:24px;margin-top:22px}
.about-copy .body{font-size:13px;line-height:22px;color:var(--muted);margin-top:16px}
.about-copy .btn{margin-top:22px;width:205px;height:50px}
.course-finder{position:absolute;left:705px;top:669px;width:416px;height:416px;background:var(--white);box-shadow:0 4px 18px rgba(0,0,0,.12)}
.course-finder h3{background:var(--red);color:var(--white);height:50px;display:flex;align-items:center;justify-content:center;font-size:20px;font-weight:500;text-transform:uppercase}
.course-finder .intro{text-align:center;font-size:13px;line-height:20px;color:var(--muted);margin:14px 90px 10px}
.finder-grid{display:grid;grid-template-columns:1fr 1fr;gap:14px 18px;padding:0 30px}
.field{height:32px;border:1px solid #ddd;display:flex;align-items:center;justify-content:space-between;padding:0 10px;font-size:12px;color:#999}
.field svg{width:10px;height:10px}
.course-finder .btn{display:flex;margin:22px 30px 0;height:44px;font-size:20px;font-weight:700}

/* features */
.features{position:absolute;top:1160px;left:0;width:1200px;height:444px}
.features .section-title{margin-top:52px}
.feature-grid{display:grid;grid-template-columns:1fr 1fr;gap:58px 60px;margin:60px 81px 0}
.feature{display:flex;gap:28px}
.feature svg{width:66px;height:60px;flex:none;color:var(--red)}
.feature h4{font-size:16px;font-weight:700;text-transform:uppercase;margin-top:6px}
.feature p{font-size:13px;line-height:20px;color:var(--muted);margin-top:8px;width:360px}

/* course blocks */
.course{position:absolute;left:0;width:1200px;height:395px;background:var(--light)}
.course.teen{top:1604px}
.course.adult{top:1999px;height:392px}
.course .photo{position:absolute;top:0;width:597px;height:100%}
.course.teen .photo{left:0;background:linear-gradient(120deg,#9fb3c4,#56606e 55%,#2d3138)}
.course.adult .photo{left:600px;background:linear-gradient(120deg,#d8dde3,#8a96a6 50%,#394556)}
.course .panel{position:absolute;top:0;width:600px;height:100%}
.course.teen .panel{left:600px}
.course.adult .panel{left:0}
.course h3{background:var(--red);color:var(--white);height:63px;display:flex;align-items:center;justify-content:center;font-size:30px;font-weight:500}
.course .panel p{font-size:13px;line-height:21px;color:var(--muted);margin:90px 65px 0}
.course .btn{margin:30px 65px 0;width:205px;height:50px}

/* plans */
.plans{position:absolute;top:2391px;left:0;width:1200px;height:564px}
.plans .section-title{margin-top:57px}
.plan-grid{position:absolute;top:129px;left:81px;width:1040px;display:grid;grid-template-columns:repeat(4,1fr);gap:4px}
.plan{height:368px;background:var(--light);text-align:center;position:relative}
.plan h3{background:var(--red);color:var(--white);height:42px;display:flex;align-items:center;justify-content:center;font-size:20px;font-weight:500}
.plan .price{font-family:"Ubuntu",sans-serif;font-size:48px;font-weight:700;margin-top:32px}
.plan ul{list-style:none;font-size:12px;line-height:24px;color:var(--muted);margin-top:14px;text-transform:uppercase}
.plan .btn{margin-top:38px;width:125px;height:46px}
.seller-badge{position:absolute;top:-22px;left:6px;width:70px;height:70px;border-radius:50%;background:var(--white);border:3px solid var(--red);display:flex;flex-direction:column;align-items:center;justify-content:center;font-family:"Ubuntu",sans-serif;font-weight:700;font-size:11px;line-height:12px;color:var(--ink)}

/* testimonials */
.testimonials{position:absolute;top:2955px;left:0;width:1200px;height:428px;background:linear-gradient(180deg,#3a3a3a,#2a2a2a 60%,#1d1d1d);text-align:center;color:var(--white)}
.testimonials h2{font-size:30px;font-weight:500;margin-top:42px}
.testimonials blockquote{width:660px;margin:28px auto 0;font-size:14px;line-height:24px;position:relative}
.quote-mark{position:absolute;font-family:"Ubuntu",sans-serif;font-size:48px;line-height:1;font-weight:700}
.quote-mark.open{left:-28px;top:-6px}
.quote-mark.close{right:-28px;bottom:-30px}
.testimonials .name{font-family:"Ubuntu",sans-serif;font-size:22px;font-weight:500;margin-top:24px}
.stars{color:var(--yellow);font-size:16px;letter-spacing:3px;margin-top:4px}
.dots{display:flex;gap:12px;justify-content:center;margin-top:18px}
.dots span{width:7px;height:7px;border-radius:50%;background:var(--white)}
.testimonials .btn{margin-top:32px;width:205px;height:50px}

/* blog */
.blog{position:absolute;top:3383px;left:0;width:1200px;height:729px}
.blog .section-title{margin-top:52px}
.post-grid{position:absolute;top:123px;left:81px;width:1040px;display:grid;grid-template-columns:repeat(3,1fr);gap:13px}
.post{background:var(--light);height:434px}
.post .thumb{height:208px}
.post:nth-child(1) .thumb{background:linear-gradient(135deg,#dfe4ea,#8e97a5)}
.post:nth-child(2) .thumb{background:linear-gradient(135deg,#6f8fb0,#2b3647)}
.post:nth-child(3) .thumb{background:linear-gradient(135deg,#c7cdd3,#4a4f58)}
.post-body{padding:20px 30px}
.post h4{font-size:15px;font-weight:500}
.post .meta{display:flex;gap:22px;font-size:11px;color:var(--muted);margin-top:8px}
.post .meta span::before{content:"";display:inline-block;width:8px;height:8px;border-radius:50%;background:var(--red);margin-right:6px}
.post p{font-size:12px;line-height:20px;color:var(--muted);margin-top:12px}
.post .more{display:inline-block;font-family:"Ubuntu",sans-serif;font-weight:700;font-size:13px;margin-top:18px;color:var(--ink);text-decoration:none}
.blog>.btn{position:absolute;left:497px;top:633px;width:205px;height:50px}

/* footer */
.site-footer{position:absolute;top:4112px;left:0;width:1200px;height:411px;background:var(--dark);color:var(--white)}
.footer-cols{position:absolute;top:74px;left:81px;width:1040px;display:flex}
.footer-cols h4{font-size:24px;font-weight:500;margin-bottom:24px}
.col-brand{width:326px}
.col-brand p{font-size:12px;line-height:20px;width:230px}
.col-brand .more{display:block;color:var(--yellow);font-weight:700;font-size:13px;margin-top:12px;text-decoration:none}
.social{display:flex;gap:16px;margin-top:40px}
.social span{width:12px;height:12px;border-radius:50%;background:#9a9a9a}
.col-links{width:226px}
.col-links ul{list-style:none;font-size:13px;line-height:20px}
.col-contact{width:226px}
.contact-row{display:flex;gap:8px;align-items:flex-start;font-size:12px;line-height:18px;margin-bottom:6px}
.contact-row svg{width:12px;height:12px;flex:none;margin-top:3px;color:var(--red)}
.contact-row.hours{color:var(--red)}
.col-news{width:262px}
.email-box{height:52px;background:var(--white);color:#999;font-size:12px;display:flex;align-items:center;padding:0 14px}
.col-news .btn{display:flex;width:100%;height:52px;margin-top:8px;font-size:15px}
.footer-rule{position:absolute;top:4345px;left:81px;width:1040px;height:1px;background:#3a3a3a}
.copyright{position:absolute;top:4434px;left:0;width:1200px;text-align:center;font-size:11px;color:#bbb}
</style>
</head>
<body>

<header class="site-header">
  <div class="brand">Kelmora Wheel Academy</div>
  <nav class="nav">
    <a class="active" href="#">Home</a><a href="#">About us</a><a href="#">Teen courses</a><a href="#">Adult courses</a><a href="#">Blog</a><a href="#">FAQs</a><a href="#">Contact us</a>
  </nav>
</header>

<section class="hero" role="img" aria-label="Instructor guiding a smiling teen student at the wheel of a car">
  <div class="hero-copy">
    <h1>Want to learn drive?</h1>
    <p>We are experts in teen driving education in Fairfax, Chantilly, Centreville, and Herndon and the greater Northern Virginia area.</p>
    <a class="btn" href="#">Call: 555-214-7730</a>
  </div>
</section>

<section class="about">
  <div class="about-copy">
    <h2>About us</h2>
    <p class="lead">We are experts in teen driving education in Fairfax, Chantilly, Centreville, and Herndon and the greater Northern Virginia area.</p>
    <p class="body">Kelmora Wheel Academy specializes in Behind the Wheel for Teens and Adults, Learners Permits, and Drivers Education.</p>
    <a class="btn" href="#">Read more</a>
  </div>
</section>

<form class="course-finder">
  <h3>Find driving courses</h3>
  <p class="intro">Send us your details and we'll find the best schedule for you!</p>
  <div class="finder-grid">
    <div class="field">Name</div><div class="field">Last Name</div>
    <div class="field">Email</div><div class="field">Phone</div>
    <div class="field">City</div><div class="field">Payment Method <svg viewBox="0 0 10 10"><path d="M1 3l4 4 4-4" fill="none" stroke="#999"/></svg></div>
    <div class="field">Course <svg viewBox="0 0 10 10"><path d="M1 3l4 4 4-4" fill="none" stroke="#999"/></svg></div><div class="field">Age <svg viewBox="0 0 10 10"><path d="M1 3l4 4 4-4" fill="none" stroke="#999"/></svg></div>
    <div class="field">Date <svg viewBox="0 0 10 10"><path d="M1 3l4 4 4-4" fill="none" stroke="#999"/></svg></div><div class="field">Time <svg viewBox="0 0 10 10"><path d="M1 3l4 4 4-4" fill="none" stroke="#999"/></svg></div>
  </div>
  <a class="btn" href="#">Find course</a>
</form>

<section class="features">
  <h2 class="section-title">The Most Advanced Driving School in Virginia</h2>
  <div class="feature-grid">
    <div class="feature">
      <svg viewBox="0 0 66 60" fill="none" stroke="currentColor" stroke-width="3"><rect x="6" y="16" width="48" height="34" rx="4"/><path d="M14 16l26-10 6 10"/><rect x="40" y="27" width="18" height="12" rx="2"/><path d="M22 28v14M18 31h7M18 39h7"/></svg>
      <div><h4>Affordable</h4><p>You have nothing to worry about, as our services are affordable and flexible</p></div>
    </div>
    <div class="feature">
      <svg viewBox="0 0 66 60" fill="none" stroke="currentColor" stroke-width="3"><path d="M4 22l12-8 10 4 8-4 10 2 18 8-6 12-10 10-12 4-14-8-10-6z"/><path d="M24 32l8 8M30 28l8 8M36 26l8 8"/></svg>
      <div><h4>Experience</h4><p>We offer private 1-on-1 lessons and customize training</p></div>
    </div>
    <div class="feature">
      <svg viewBox="0 0 66 60" fill="none" stroke="currentColor" stroke-width="3"><circle cx="33" cy="22" r="14"/><circle cx="33" cy="22" r="7"/><path d="M24 33l-6 22 8-4 5 7 4-12M42 33l6 22-8-4-5 7"/></svg>
      <div><h4>Guarantee</h4><p>We guarantee 100% satisfaction and premium training from our instructors</p></div>
    </div>
    <div class="feature">
      <svg viewBox="0 0 66 60" fill="none" stroke="currentColor" stroke-width="3"><path d="M12 4h32l10 10v42H12z"/><path d="M20 18h24M20 26h24M20 34h12"/><circle cx="40" cy="42" r="6"/><path d="M36 47l-2 8 6-3 6 3-2-8"/></svg>
      <div><h4>Certified</h4><p>All of our instructors are certified by the State Motor Vehicle Office</p></div>
    </div>
  </div>
</section>

<section class="course teen">
  <div class="photo" role="img" aria-label="Two teenagers practicing driving in a car"></div>
  <div class="panel">
    <h3>Teen Course</h3>
    <p>Lorem Ipsum is simply dummy text of the printing and typesetting industry. Lorem Ipsum has been the industry's standard dummy text ever since the 1500s, when an unknown printer took a galley of type and scrambled it to make a type specimen book. It has survived not only five centuries, but also the leap into electronic typesetting, remaining essentially unchanged.</p>
    <a class="btn" href="#">Learn more</a>
  </div>
</section>

<section class="course adult">
  <div class="panel">
    <h3>Adult Course</h3>
    <p>Lorem Ipsum is simply dummy text of the printing and typesetting industry. Lorem Ipsum has been the industry's standard dummy text ever since the 1500s, when an unknown printer took a galley of type and scrambled it to make a type specimen book. It has survived not only five centuries, but also the leap into electronic typesetting, remaining essentially unchanged.</p>
    <a class="btn" href="#">Learn more</a>
  </div>
  <div class="photo" role="img" aria-label="Happy adult driver giving a thumbs up from the driver's seat"></div>
</section>

<section class="plans">
  <h2 class="section-title">Choose Your Plan</h2>
  <div class="plan-grid">
    <div class="plan"><h3>Silver</h3><div class="price">$399</div><ul><li>5 - 60 minutes lessons</li><li>A pre-licensing class</li><li>A road test appointment</li><li>A car for road test</li></ul><a class="btn" href="#">Book now</a></div>
    <div class="plan"><div class="seller-badge"><span>BEST</span><span>SELLER</span></div><h3>Diamond</h3><div class="price">$644</div><ul><li>10 - 60 minutes lessons</li><li>A pre-licensing class</li><li>A road test appointment</li><li>A car for road test</li></ul><a class="btn" href="#">Book now</a></div>
    <div class="plan"><h3>GOLD</h3><div class="price">$534</div><ul><li>8 - 60 minutes lessons</li><li>A pre-licensing class</li><li>A road test appointment</li><li>A car for road test</li></ul><a class="btn" href="#">Book now</a></div>
    <div class="plan"><div class="seller-badge"><span>BEST</span><span>SELLER</span></div><h3>PLATINUM</h3><div class="price">$899</div><ul><li>15 - 60 minutes lessons</li><li>A pre-licensing class</li><li>A road test appointment</li><li>A car for road test</li></ul><a class="btn" href="#">Book now</a></div>
  </div>
</section>

<section class="testimonials" role="img" aria-label="Darkened background of a student car on the road">
  <h2>Testimonials</h2>
  <blockquote>
    <span class="quote-mark open">&ldquo;</span>
    Lorem Ipsum is simply dummy text of the printing and typesetting industry. Lorem Ipsum has been the industry's standard dummy text ever since the 1500s, when an unknown printer took a galley of type and scrambled it to make a type specimen book.
    <span class="quote-mark close">&rdquo;</span>
  </blockquote>
  <div class="name">Dana Merrow</div>
  <div class="stars">★★★★★</div>
  <div class="dots"><span></span><span></span><span></span></div>
  <a class="btn" href="#">View all</a>
</section>

<section class="blog">
  <h2 class="section-title">Blog Posts</h2>
  <div class="post-grid">
    <article class="post"><div class="thumb" role="img" aria-label="Instructor teaching a driving theory class"></div><div class="post-body"><h4>Blog Posts # 01</h4><div class="meta"><span>April 19,2019</span><span>Comments (15)</span></div><p>Lorem Ipsum is simply dummy text of the printing and typesetting industry. Lorem Ipsum has been the industry's standard dummy text ever since the 1500s.</p><a class="more" href="#">READ MORE..</a></div></article>
    <article class="post"><div class="thumb" role="img" aria-label="Student and instructor inside a car"></div><div class="post-body"><h4>Blog Posts # 02</h4><div class="meta"><span>April 19,2019</span><span>Comments (15)</span></div><p>Lorem Ipsum is simply dummy text of the printing and typesetting industry. Lorem Ipsum has been the industry's standard dummy text ever since the 1500s.</p><a class="more" href="#">READ MORE..</a></div></article>
    <article class="post"><div class="thumb" role="img" aria-label="Car on a practice course with traffic cones"></div><div class="post-body"><h4>Blog Posts # 03</h4><div class="meta"><span>April 19,2019</span><span>Comments (15)</span></div><p>Lorem Ipsum is simply dummy text of the printing and typesetting industry. Lorem Ipsum has been the industry's standard dummy text ever since the 1500s.</p><a class="more" href="#">READ MORE..</a></div></article>
  </div>
  <a class="btn" href="#">Read more</a>
</section>

<footer class="site-footer">
  <div class="footer-cols">
    <div class="col-brand">
      <h4>Kelmora Wheel Academy</h4>
      <p>We are experts in teen driving education in Fairfax, Chantilly, Centreville, and Herndon and the greater Northern Virginia area.</p>
      <a class="more" href="#">READ MORE..</a>
      <div class="social"><span></span><span></span><span></span><span></span><span></span></div>
    </div>
    <div class="col-links">
      <h4>Quick Links</h4>
      <ul><li>Home</li><li>About us</li><li>Teen courses</li><li>Adult courses</li><li>Blog</li><li>FAQs</li><li>Contact us</li></ul>
    </div>
    <div class="col-contact">
      <h4>Contact Info..</h4>
      <div class="contact-row"><svg viewBox="0 0 12 12"><path d="M6 0a4 4 0 0 0-4 4c0 3 4 8 4 8s4-5 4-8a4 4 0 0 0-4-4z" fill="currentColor"/></svg><span>48 Hollin Row<br>Brantmere, GA 30512</span></div>
      <div class="contact-row"><svg viewBox="0 0 12 12"><path d="M2 1l3 0 1 3-2 1a7 7 0 0 0 3 3l1-2 3 1v3c-6 0-10-4-9-9z" fill="currentColor"/></svg><span>555-214-7730</span></div>
      <div class="contact-row"><svg viewBox="0 0 12 12"><rect x="0" y="2" width="12" height="8" fill="currentColor"/></svg><span>info@kelmorawheelacademy.com</span></div>
      <div class="contact-row hours"><svg viewBox="0 0 12 12"><circle cx="6" cy="6" r="5" fill="none" stroke="currentColor" stroke-width="1.5"/><path d="M6 3v3h2" stroke="currentColor" fill="none"/></svg><span>Working Hours</span></div>
      <div class="contact-row"><span>Mon - Fri 8:00 AM - 7:00 PM</span></div>
    </div>
    <div class="col-news">
      <h4>Newsletter</h4>
      <div class="email-box">Email Address</div>
      <a class="btn" href="#">Subscribe now</a>
    </div>
  </div>
  <div class="footer-rule"></div>
</footer>
<div class="copyright">Copyright © 2019 Kelmora Wheel Academy All Rights Reserved Terms of Use and Privacy Policy</div>

</body>
</html>
```